REALTOR POSTCARD HANDOUT

I AM A MORTGAGE COMPANY...THIS WILL BE A HANDOUT ON A LARGE POSTCARD THAT I WILL BE GIVING OUT AT OPEN HOUSES.IT WILL HAVE VARIOUS NICHES THAT I FUND THAT MOST OTHER LENDERS DONT FUND...

Industry/Entity Type

It Company

Logo Text

KVO (STAND FOR KESTREL VALLEY ORCHARD)

Logo styles of interest
Lettermark Logo
Requirements
Must have
• I WANT IT TO BE A VERY BRIGHT AND VIDID POSTCARD...I MIGHT HAVE A MORTGAGE CALUCALTOR ON THE BACK OF THE CARD POSSIBLY....
Nice to have
• LOTS OF COLORS..BUT CLASSY AS WELL..IT WILL BE EMBOSSED
POSSIBLE GRAPHICS..BUT NOT TOO BUSY....

```html
<!DOCTYPE html>
<html lang="en">
<head>
<meta charset="utf-8">
<title>Kestrel Valley Orchard – Realtor Postcard</title>
<link rel="stylesheet" href="https://fonts.googleapis.com/css2?family=Cinzel:wght@400;600&family=Didact+Gothic&display=swap">
<style>
  :root {
    --navy: #0b1150;
    --panel-top: #1f8fd0;
    --panel-bottom: #0a63a6;
    --sky-light: #8cc6f2;
    --sky-deep: #1c58b8;
    --white: #ffffff;
    --page: #ffffff;
    --card: #f4f6f9;
    --icon: #0a3d7a;
  }
  * { margin: 0; padding: 0; box-sizing: border-box; }
  html, body { width: 1200px; height: 1000px; overflow: hidden; background: var(--page); }
  .canvas { position: relative; width: 1200px; height: 1000px; background: var(--page); }
  .postcard {
    position: absolute; left: 0; top: 78px; width: 1200px; height: 768px;
    background: linear-gradient(180deg, var(--white) 0%, var(--card) 100%);
    border: 1px solid #999;
    overflow: hidden;
  }
  .headline {
    position: absolute; left: 22px; right: 22px; top: 12px; height: 58px;
    border-top: 2px solid var(--navy);
    font-family: "Cinzel", serif; font-weight: 400; color: var(--navy);
    font-size: 50px; line-height: 54px; text-align: center; letter-spacing: 2px;
    white-space: nowrap;
  }
  .tagline-band {
    position: absolute; left: 0; top: 70px; width: 1200px; height: 54px;
  }
  .tagline-band svg { position: absolute; inset: 0; }
  .tagline {
    position: absolute; inset: 0; padding-top: 4px;
    font-family: "Didact Gothic", sans-serif; color: var(--white);
    -webkit-text-stroke: 0.8px var(--white);
    font-size: 36px; line-height: 50px; text-align: center; letter-spacing: 2px;
    white-space: nowrap;
  }
  .hero-photo {
    position: absolute; left: 28px; top: 135px; width: 395px; height: 449px; z-index: 2;
    border: 2px solid var(--navy);
    background: radial-gradient(circle at 85% 5%, #ffffff 0%, var(--sky-light) 25%, var(--sky-deep) 75%, #2d6fc4 100%);
  }
  .niche-panel {
    position: absolute; left: 423px; top: 146px; width: 750px; height: 416px;
    border-radius: 0 10px 10px 0;
    background: linear-gradient(160deg, var(--panel-top) 0%, var(--panel-bottom) 100%);
  }
  .niche-list {
    list-style: none; position: absolute; left: 26px; top: 22px;
    font-family: "Didact Gothic", sans-serif; color: var(--white);
    -webkit-text-stroke: 0.7px var(--white);
    font-size: 30px; line-height: 38.3px; letter-spacing: 1.1px;
    white-space: nowrap;
  }
  .niche-list li { position: relative; padding-left: 44px; }
  .niche-list li svg { position: absolute; left: 0; top: 5px; width: 28px; height: 28px; }
  .license {
    position: absolute; right: 16px; bottom: -2px;
    font-family: "Didact Gothic", sans-serif; color: var(--white);
    -webkit-text-stroke: 0.4px var(--white); font-size: 19px;
  }
  .contact-band {
    position: absolute; left: 0; top: 577px; width: 1200px; height: 191px;
    background: var(--navy);
  }
  .signer {
    position: absolute; left: 32px; top: 53px; width: 768px;
    border-top: 2px solid var(--white); border-bottom: 2px solid var(--white);
    font-family: "Cinzel", serif; font-weight: 400; color: var(--white);
    font-size: 50px; line-height: 58px; text-align: center; letter-spacing: 1px;
    white-space: nowrap;
  }
  .contact-line {
    position: absolute; left: 82px; top: 126px;
    font-family: "Didact Gothic", sans-serif; color: var(--white);
    -webkit-text-stroke: 0.6px var(--white);
    font-size: 30px; letter-spacing: 0.8px; white-space: nowrap;
  }
  .brand {
    position: absolute; left: 858px; top: 48px; width: 310px; text-align: center;
    font-family: "Cinzel", serif; font-weight: 400; color: var(--white);
  }
  .brand-mark { font-size: 88px; line-height: 92px; letter-spacing: 4px; }
  .brand-name { font-size: 17px; letter-spacing: 1.5px; margin-top: 4px; }
</style>
</head>
<body>
<div class="canvas">
  <section class="postcard">
    <h1 class="headline">HELPING REALTORS CLOSE MORE ESCROWS!</h1>

    <div class="tagline-band">
      <svg width="1200" height="54" viewBox="0 0 1200 54" aria-hidden="true">
        <path d="M22 0 H1178 V42 Q1178 54 1166 54 H34 Q22 54 22 42 Z" fill="var(--navy)"/>
        <path d="M22 5 H1178" stroke="#ffffff" stroke-width="1.5"/>
      </svg>
      <p class="tagline">ONE LOAN AT A TIME! LOAN PROGRAM NICHES WE OFFER</p>
    </div>

    <div class="hero-photo" role="img" aria-label="Photo of an open hand under a blue sky with clouds shaped like a house, a dollar sign, a family and a car"></div>

    <div class="niche-panel">
      <ul class="niche-list">
        <li><svg viewBox="0 0 28 28" aria-hidden="true"><circle cx="14" cy="14" r="13" fill="var(--icon)" stroke="#fff" stroke-width="2"/><path d="M8 15 l4 4 l8 -9" fill="none" stroke="#fff" stroke-width="2.5"/></svg>Stated Income Loans..No Pay Stubs,<br>No Tax Returns, No W2s..No Problem!</li>
        <li><svg viewBox="0 0 28 28" aria-hidden="true"><circle cx="14" cy="14" r="13" fill="var(--icon)" stroke="#fff" stroke-width="2"/><path d="M8 15 l4 4 l8 -9" fill="none" stroke="#fff" stroke-width="2.5"/></svg>Past Short Sale, Bankruptcies,<br>Foreclosures Ok</li>
        <li><svg viewBox="0 0 28 28" aria-hidden="true"><circle cx="14" cy="14" r="13" fill="var(--icon)" stroke="#fff" stroke-width="2"/><path d="M8 15 l4 4 l8 -9" fill="none" stroke="#fff" stroke-width="2.5"/></svg>Kvo Loans Down To A 500 Vero Score</li>
        <li><svg viewBox="0 0 28 28" aria-hidden="true"><circle cx="14" cy="14" r="13" fill="var(--icon)" stroke="#fff" stroke-width="2"/><path d="M8 15 l4 4 l8 -9" fill="none" stroke="#fff" stroke-width="2.5"/></svg>14 Day Escrow Closings! We Close Fast!</li>
        <li><svg viewBox="0 0 28 28" aria-hidden="true"><circle cx="14" cy="14" r="13" fill="var(--icon)" stroke="#fff" stroke-width="2"/><path d="M8 15 l4 4 l8 -9" fill="none" stroke="#fff" stroke-width="2.5"/></svg>Your Customers Loan Declined? Call Us!<br>We Can Help!</li>
        <li><svg viewBox="0 0 28 28" aria-hidden="true"><circle cx="14" cy="14" r="13" fill="var(--icon)" stroke="#fff" stroke-width="2"/><path d="M8 15 l4 4 l8 -9" fill="none" stroke="#fff" stroke-width="2.5"/></svg>Loans With No Closing Costs Offered</li>
        <li><svg viewBox="0 0 28 28" aria-hidden="true"><circle cx="14" cy="14" r="13" fill="var(--icon)" stroke="#fff" stroke-width="2"/><path d="M8 15 l4 4 l8 -9" fill="none" stroke="#fff" stroke-width="2.5"/></svg>Low Rates!</li>
      </ul>
      <p class="license">License No. 418273</p>
    </div>

    <footer class="contact-band">
      <h2 class="signer">Dale Ashcombe/President</h2>
      <p class="contact-line">kvolending1@orchardmail.com | (805) 555-0148</p>
      <div class="brand">
        <div class="brand-mark">KVO</div>
        <div class="brand-name">KESTREL VALLEY ORCHARD</div>
      </div>
    </footer>
  </section>
</div>
</body>
</html>
```